Crowdfunding a casino! Lotrafy.io

looking for an attractive flashy design that sells a casino idea that needs crowdfunding. need a custom logo int he design as well that's why we offer a high price :)

```html
<!DOCTYPE html>
<html lang="en">
<head>
<meta charset="utf-8">
<title>Lotrafy.io – The Future of Metaverse Casinos</title>
<link rel="stylesheet" href="https://fonts.googleapis.com/css2?family=Archivo:wght@700;800;900&family=Inter:wght@400;500;600;700&display=swap">
<style>
:root{
  --pink:#ff2e72;
  --pink-dark:#c81a55;
  --ink:#0c0f14;
  --ink-2:#12151c;
  --navy:#1b1e2e;
  --navy-2:#161927;
  --white:#ffffff;
  --muted:#d5d7de;
  --line:#2a2e3a;
}
*{box-sizing:border-box;margin:0;padding:0}
html,body{width:1200px;height:4843px;overflow:hidden}
body{background:var(--ink);color:var(--white);font-family:"Inter",sans-serif;position:relative}
section,header,footer{position:absolute;left:0;width:1200px}
.abs{position:absolute}
h1,h2,h3,h4,.logo{font-family:"Archivo",sans-serif;font-weight:800;text-transform:uppercase}
.logo{text-transform:none;font-weight:800;font-size:25px;color:var(--white)}
.pink{color:var(--pink)}
.btn{position:absolute;display:flex;align-items:center;justify-content:center;gap:12px;background:var(--pink);color:var(--white);font-family:"Inter",sans-serif;font-weight:700;font-size:14px;text-transform:uppercase;box-shadow:5px 5px 0 var(--pink-dark);letter-spacing:.2px}
.btn svg{width:16px;height:16px}
.ph{position:absolute}

/* top bar */
.topbar{top:0;height:51px;background:var(--navy)}
.topbar .item{position:absolute;top:0;height:51px;display:flex;align-items:center;gap:10px;font-size:14px}
.topbar svg,.footer svg.ico{width:15px;height:15px;fill:var(--pink)}
.socials-mini{position:absolute;right:85px;top:19px;display:flex;gap:14px}
.socials-mini span{width:12px;height:12px;border:2px solid var(--white);border-radius:50%}

/* nav */
.nav{top:51px;height:90px;background:var(--navy-2)}
.nav .logo{position:absolute;left:85px;top:31px}
.menu{position:absolute;left:401px;top:36px;display:flex;gap:36px;font-size:14px;font-weight:700;text-transform:uppercase}
.menu .active{color:var(--pink)}

/* hero */
.hero{top:141px;height:564px;background:#0a0b0e}
.hero-art{left:565px;top:0;width:635px;height:564px;background:radial-gradient(ellipse at 55% 55%,#6b3a12 0%,#3a1f0c 30%,#140c08 60%,#0a0b0e 80%)}
.hero h1{position:absolute;left:85px;top:133px;font-size:55px;line-height:58px;font-weight:900}
.hero .sub{position:absolute;left:85px;top:315px;font-size:22px;font-weight:600}
.dots{position:absolute;left:569px;top:521px;display:flex;gap:14px}
.dots span{width:13px;height:13px;border:2px solid #aaa}
.dots .on{background:var(--white);border-color:var(--white)}

/* why */
.why{top:705px;height:649px;background:#0b0c0f}
.why-art{left:0;top:0;width:527px;height:649px;background:radial-gradient(ellipse at 50% 40%,#7a1414 0%,#3a0d10 35%,#161619 70%,#0b0c0f 100%)}
.why .frame{position:absolute;left:126px;top:66px;width:335px;height:380px;border-left:9px solid var(--pink);border-top:9px solid var(--pink);border-bottom:9px solid var(--pink)}
.why .vtext{position:absolute;left:447px;top:455px;transform:rotate(-90deg);transform-origin:left top;font-family:"Archivo",sans-serif;font-weight:900;font-size:24px;white-space:nowrap}
.why h2{position:absolute;left:600px;top:130px;font-size:37px}
.body-copy{font-size:16.5px;line-height:27px;color:var(--muted)}
.why .body-copy{position:absolute;left:600px;top:183px;width:515px}

/* how */
.how{top:1354px;height:668px;background:var(--ink-2)}
.eyebrow{font-size:15px;font-weight:500;letter-spacing:.5px}
.how .eyebrow{position:absolute;left:0;width:1200px;text-align:center;top:92px}
.how h2{position:absolute;left:0;width:1200px;text-align:center;top:118px;font-size:37px}
.step{position:absolute;width:489px;display:flex;gap:20px}
.step .num{flex:none;width:55px;height:55px;border:2px dashed var(--pink);display:flex;align-items:center;justify-content:center;font-family:"Archivo",sans-serif;font-weight:800;font-size:24px}
.step p{font-size:16.5px;line-height:27px;color:var(--muted);padding-top:2px}
.rule{position:absolute;height:1px;background:var(--line)}
.how .pinkrule{position:absolute;left:85px;top:578px;width:1030px;height:3px;background:var(--pink)}
.btn.light{background:var(--white);color:var(--pink);box-shadow:5px 5px 0 var(--pink)}

/* rounds */
.rounds{top:2022px;height:649px;background:#0d0f13}
.rounds .eyebrow{position:absolute;left:85px;top:128px}
.rounds h2{position:absolute;left:85px;top:150px;font-size:37px}
.round{position:absolute;top:254px;width:300px}
.round .badge{position:relative;width:110px;height:110px;border-radius:50%;border:2px solid #3a3d47;display:flex;align-items:center;justify-content:center;color:var(--pink);font-family:"Archivo",sans-serif;font-weight:900;font-size:30px}
.round .badge::after{content:"";position:absolute;right:-30px;top:52px;width:42px;height:42px;border-radius:50%;background:linear-gradient(90deg,var(--pink) 50%,#24262d 50%)}
.round h4{margin-top:42px;font-size:17px}
.round .tag{margin-top:18px;color:var(--pink);font-weight:600;font-size:16px}
.round p{font-size:16px;line-height:27px;color:var(--muted)}

/* banking */
.banking{top:2671px;height:536px;background:#0d0f13}
.bank-art{left:0;top:38px;width:611px;height:498px;background:radial-gradient(ellipse at 55% 45%,#6d2a1a 0%,#3a1a16 35%,#17151a 70%,#0d0f13 100%)}
.banking .frame{position:absolute;left:463px;top:83px;width:150px;height:350px;border-left:9px solid var(--pink);border-top:9px solid var(--pink);border-bottom:9px solid var(--pink);border-right:0}
.banking .vtext{position:absolute;left:412px;top:175px;transform:rotate(-90deg);transform-origin:left top;font-family:"Archivo",sans-serif;font-weight:900;font-size:22px;white-space:nowrap}
.banking h2{position:absolute;left:685px;top:72px;width:440px;font-size:28px;line-height:41px}
.banking .tag{position:absolute;left:685px;top:205px;width:420px;color:var(--pink);font-weight:600;font-size:16.5px;line-height:28px}
.banking .body-copy{position:absolute;left:685px;top:276px;width:430px}

/* strengths */
.strengths{top:3207px;height:677px;background:var(--ink-2)}
.strengths h2{position:absolute;left:0;width:1200px;text-align:center;top:94px;font-size:37px}
.card{position:absolute;top:183px;width:326px;height:396px;border:2px solid var(--pink);border-radius:8px;overflow:hidden;background:#0f1116;text-align:center}
.card .art{position:relative;height:226px;margin:6px 6px 0}
.card h3{margin-top:52px;font-size:17px}
.card p{margin:14px auto 0;width:260px;font-size:16px;line-height:27px;color:var(--muted)}

/* contact */
.contact{top:3884px;height:530px;background:radial-gradient(ellipse at 50% 100%,#2a2d33 0%,#15171c 45%,#0d0f13 80%)}
.contact .bracket{position:absolute;left:85px;top:91px;width:201px;height:355px;border-left:8px solid var(--white);border-top:0;border-bottom:8px solid var(--white)}
.contact .bracket::before{content:"";position:absolute;left:-8px;top:0;width:73px;height:8px;background:var(--white)}
.contact .bracket::after{content:"";position:absolute;right:0;bottom:0;width:8px;height:88px;background:var(--white)}
.contact h2{position:absolute;left:132px;top:138px;font-size:37px}
.contact .body-copy{position:absolute;left:132px;top:200px;width:430px;font-size:16px}
.circles{position:absolute;left:132px;top:298px;display:flex;gap:9px}
.circles span{width:52px;height:52px;border-radius:50%;border:2px solid var(--pink)}
.field{position:absolute;background:var(--white);color:#3a3a3a;font-size:15px;padding:15px 18px}
.contact-line{top:4414px;height:5px;background:var(--pink)}

/* footer */
.footer{top:4419px;height:424px;background:var(--navy-2)}
.footer .logo{position:absolute;left:85px;top:68px}
.footer .contacts{position:absolute;left:85px;top:133px;display:flex;flex-direction:column;gap:26px;font-size:16px}
.footer .contacts div{display:flex;align-items:center;gap:16px}
.fcol{position:absolute;top:76px}
.fcol h4{font-size:16px;margin-bottom:25px}
.fcol a{display:block;color:var(--white);text-decoration:none;font-size:16px;line-height:30px}
.copy{position:absolute;left:0;width:1200px;top:358px;text-align:center;font-size:15px;font-weight:600}
</style>
</head>
<body>

<header class="topbar">
  <div class="item" style="left:85px">
    <svg viewBox="0 0 24 24"><path d="M2 5h20v14H2z M2 5l10 8 10-8" fill="none" stroke="#ff2e72" stroke-width="2.5"/></svg>
    hello@lotrafy.io
  </div>
  <div class="item" style="left:298px">
    <svg viewBox="0 0 24 24"><path d="M12 2a7 7 0 0 0-7 7c0 5 7 13 7 13s7-8 7-13a7 7 0 0 0-7-7zm0 9.5A2.5 2.5 0 1 1 12 6.5a2.5 2.5 0 0 1 0 5z"/></svg>
    42 Harbor Lane, USA
  </div>
  <div class="item" style="left:855px">
    <svg viewBox="0 0 24 24"><path d="M6.6 10.8a15.1 15.1 0 0 0 6.6 6.6l2.2-2.2a1 1 0 0 1 1-.25 11.4 11.4 0 0 0 3.6.57 1 1 0 0 1 1 1V20a1 1 0 0 1-1 1A17 17 0 0 1 3 4a1 1 0 0 1 1-1h3.5a1 1 0 0 1 1 1c0 1.25.2 2.45.57 3.6a1 1 0 0 1-.25 1z"/></svg>
    555-010-2468
  </div>
  <div class="socials-mini"><span></span><span></span><span></span><span></span></div>
</header>

<header class="nav">
  <div class="logo">Lotrafy.io</div>
  <nav class="menu">
    <span class="active">Home</span><span>About us</span><span>Ouer strength</span><span>Blog</span><span>Contact</span>
  </nav>
  <div class="btn" style="left:953px;top:23px;width:162px;height:44px;box-shadow:none">Let's talk
    <svg viewBox="0 0 20 20"><circle cx="10" cy="10" r="9" fill="#fff"/><path d="M7 10h6M10 7l3 3-3 3" stroke="#ff2e72" stroke-width="2" fill="none"/></svg>
  </div>
</header>

<section class="hero">
  <div class="ph hero-art" role="img" aria-label="Glowing golden playing cards, roulette wheel, dice and chips"></div>
  <h1>The future<br>of metaverse<br><span class="pink">casinos</span> awaits.</h1>
  <p class="sub">Invest Now, and Share the Wins Tomorrow!</p>
  <div class="btn" style="left:85px;top:367px;width:197px;height:51px">Get started
    <svg viewBox="0 0 20 20"><circle cx="10" cy="10" r="9" fill="#fff"/><path d="M7 10h6M10 7l3 3-3 3" stroke="#ff2e72" stroke-width="2" fill="none"/></svg>
  </div>
  <div class="dots"><span></span><span class="on"></span><span></span></div>
</section>

<section class="why">
  <div class="ph why-art" role="img" aria-label="Woman in a red satin dress holding playing cards beside casino chips"></div>
  <div class="frame"></div>
  <div class="vtext">Top class <span class="pink">casino ideas</span></div>
  <h2>Why metaverse <span class="pink">casino?</span></h2>
  <div class="body-copy">
    <p>Picture a world where traditional casino gaming meets the innovation of the MetaVerse. That's what Lotrafy.io is bringing to the table. A seamlessly integrated experience where online betting enters a limitless digital realm, expanding with boundless possibilities.</p>
    <p style="margin-top:26px">From blackjack tables set amidst virtual jungles to roulette nestled within mountain terrains, the MetaVerse Casino doesn't just offer games - it offers experiences.</p>
  </div>
  <div class="btn" style="left:600px;top:455px;width:193px;height:51px">Contact us
    <svg viewBox="0 0 20 20"><circle cx="10" cy="10" r="9" fill="#fff"/><path d="M7 10h6M10 7l3 3-3 3" stroke="#ff2e72" stroke-width="2" fill="none"/></svg>
  </div>
</section>

<section class="how">
  <p class="eyebrow">Simple &amp; Sweet</p>
  <h2>How it <span class="pink">works</span></h2>

  <div class="step" style="left:85px;top:212px"><div class="num">01</div><p>We need a bankroll to set the wheels in motion. The strength of our casino lies in its foundational capital.</p></div>
  <div class="step" style="left:626px;top:212px"><div class="num">04</div><p>Your Return is linked directly to the casino's performance. The better we do the higher your earning.</p></div>
  <div class="rule" style="left:85px;top:295px;width:489px"></div>
  <div class="rule" style="left:626px;top:295px;width:489px"></div>

  <div class="step" style="left:85px;top:316px"><div class="num">02</div><p>Crowdfunding is our key, leveraging the dynamic world of cryptocurrency.</p></div>
  <div class="step" style="left:626px;top:316px"><div class="num">05</div><p>Early Withdrawals come with fines, incentivizing longer participation and bigger rewards.</p></div>
  <div class="rule" style="left:85px;top:400px;width:489px"></div>
  <div class="rule" style="left:626px;top:400px;width:489px"></div>

  <div class="step" style="left:85px;top:420px"><div class="num">03</div><p>Lock-in periods ensure you enjoy sustained returns. Investments will be locked for a specific duration (e.g., 2 years), during which you earn monthly from the casino's operations.</p></div>
  <div class="step" style="left:626px;top:420px"><div class="num">06</div><p>Investment cuts fuel the casino's operations, funding marketing and operational costs.</p></div>

  <div class="pinkrule"></div>
  <div class="btn light" style="left:505px;top:555px;width:185px;height:48px">View more
    <svg viewBox="0 0 20 20"><circle cx="10" cy="10" r="9" fill="#ff2e72"/><path d="M7 10h6M10 7l3 3-3 3" stroke="#fff" stroke-width="2" fill="none"/></svg>
  </div>
</section>

<section class="rounds">
  <p class="eyebrow">Investment Rounds</p>
  <h2>More than just <span class="pink">money</span></h2>

  <div class="round" style="left:85px">
    <div class="badge"><svg width="44" height="44" viewBox="0 0 24 24" fill="none" stroke="#ff2e72" stroke-width="1.8"><rect x="5" y="11" width="14" height="10" rx="1"/><path d="M8 11V8a4 4 0 0 1 8 0v3"/><circle cx="12" cy="16" r="1.4"/></svg></div>
    <h4>Round 01</h4>
    <p class="tag">Secure the bankroll.</p>
    <p>Launch our innovative Chatwave casino.</p>
  </div>
  <div class="round" style="left:453px">
    <div class="badge">777</div>
    <h4>Round 02</h4>
    <p class="tag">Bring the MetaVerse to life.</p>
    <p>Dive into the limitless expanses, owning shops, designing exclusive game levels, and even enjoying top slots in the virtual arena.</p>
  </div>
  <div class="round" style="left:820px">
    <div class="badge">%</div>
    <h4>Round 03</h4>
    <p class="tag">Expand horizons.</p>
    <p>From web versions of the casino to introducing leveraged trading and additional licenses, the sky isn't the limit - there is no limit!</p>
  </div>
</section>

<section class="banking">
  <div class="ph bank-art" role="img" aria-label="Three friends celebrating a win at a casino table with chips"></div>
  <div class="frame"></div>
  <div class="vtext">We are</div>
  <h2>What's banking offering you? A mere percentage of interest?</h2>
  <p class="tag">Dive into Lotrafy.io's realm and amplify your returns. How?</p>
  <p class="body-copy">Referrals. Bring in more investors, and skyrocket your returns. See your investments grow in real-time. Hop on now, and ensure you're at the forefront when the magic unfolds!</p>
  <div class="btn" style="left:687px;top:410px;width:193px;height:51px">Contact us
    <svg viewBox="0 0 20 20"><circle cx="10" cy="10" r="9" fill="#fff"/><path d="M7 10h6M10 7l3 3-3 3" stroke="#ff2e72" stroke-width="2" fill="none"/></svg>
  </div>
</section>

<section class="strengths">
  <h2>Strengths in our <span class="pink">stride</span></h2>
  <div class="card" style="left:85px">
    <div class="art" role="img" aria-label="Roulette wheel with cards and chips in fiery light" style="background:radial-gradient(ellipse at 50% 60%,#c4561a 0%,#5c220e 45%,#1a0e0a 85%)"></div>
    <h3>A working Chatwave casino</h3>
    <p>We're not just visionaries; we're implementers.</p>
  </div>
  <div class="card" style="left:438px">
    <div class="art" role="img" aria-label="Hand holding a card in front of glowing casino lights" style="background:radial-gradient(ellipse at 50% 50%,#8a3e1e 0%,#3d1a12 45%,#140d0c 85%)"></div>
    <h3>Affiliation programs</h3>
    <p>Marketing strategies ready to roll out.</p>
  </div>
  <div class="card" style="left:788px">
    <div class="art" role="img" aria-label="Stacks of colourful chips under neon casino lights" style="background:radial-gradient(ellipse at 50% 55%,#2e6f8a 0%,#1c2a45 45%,#120f1c 85%)"></div>
    <h3>Scheduled milestones</h3>
    <p>Set plans for MetaVerse Casino, Web Versions, and more.</p>
  </div>
</section>

<section class="contact" role="img" aria-label="Dim roulette wheel in the background">
  <div class="bracket"></div>
  <h2>Contact <span class="pink">us</span></h2>
  <p class="body-copy">All our assumptions, mathematical logic, and business models are validated, ensuring our approach is not only revolutionary but also feasible.</p>
  <div class="circles"><span></span><span></span><span></span><span></span></div>

  <div class="field" style="left:600px;top:106px;width:248px;height:48px">Name</div>
  <div class="field" style="left:865px;top:106px;width:249px;height:48px">Email address</div>
  <div class="field" style="left:600px;top:173px;width:248px;height:48px">Phone no</div>
  <div class="field" style="left:865px;top:173px;width:249px;height:48px">Subject</div>
  <div class="field" style="left:600px;top:243px;width:514px;height:119px">Leave a message</div>
  <div class="btn" style="left:600px;top:384px;width:205px;height:51px">Send message
    <svg viewBox="0 0 20 20"><circle cx="10" cy="10" r="9" fill="#fff"/><path d="M7 10h6M10 7l3 3-3 3" stroke="#ff2e72" stroke-width="2" fill="none"/></svg>
  </div>
</section>
<div class="abs contact-line" style="left:0;width:1200px"></div>

<footer class="footer">
  <div class="logo">Lotrafy.io</div>
  <div class="contacts">
    <div><svg class="ico" viewBox="0 0 24 24"><path d="M6.6 10.8a15.1 15.1 0 0 0 6.6 6.6l2.2-2.2a1 1 0 0 1 1-.25 11.4 11.4 0 0 0 3.6.57 1 1 0 0 1 1 1V20a1 1 0 0 1-1 1A17 17 0 0 1 3 4a1 1 0 0 1 1-1h3.5a1 1 0 0 1 1 1c0 1.25.2 2.45.57 3.6a1 1 0 0 1-.25 1z"/></svg>555-010-2468</div>
    <div><svg class="ico" viewBox="0 0 24 24"><path d="M12 2a7 7 0 0 0-7 7c0 5 7 13 7 13s7-8 7-13a7 7 0 0 0-7-7zm0 9.5A2.5 2.5 0 1 1 12 6.5a2.5 2.5 0 0 1 0 5z"/></svg>42 Harbor Lane, USA</div>
    <div><svg class="ico" viewBox="0 0 24 24"><path d="M2 5h20v14H2z M2 5l10 8 10-8" fill="none" stroke="#ff2e72" stroke-width="2.5"/></svg>hello@lotrafy.io</div>
  </div>
  <div class="fcol" style="left:440px"><h4>Quick link</h4><a>Home</a><a>About Us</a><a>Ouer Strength</a><a>Blog</a></div>
  <div class="fcol" style="left:696px"><h4>Other links</h4><a>Terms &amp; Condition</a><a>Cookies</a><a>Privacy Policy</a><a>FAQs</a></div>
  <div class="fcol" style="left:986px"><h4>Social links</h4><a>Circlr</a><a>Pixora</a><a>Linkwise</a><a>Searcha</a></div>
  <p class="copy">Copyright © 2023 Lotrafy. All rights reserved. &nbsp;| &nbsp;<span class="pink">Contact</span></p>
</footer>

</body>
</html>
```